Design range of flavoured vodka soda cans

We need help designing a range of flavoured vodka soda cans.
Our company is www.torlandistillery.com.au
Vodka soda flavours include;
- Raspberry
- Grape
- Blueberry
- Pina Colada
- Musk
- Lime
- Pineapple
- Watermelon
- Tropical Punch
- Honeycomb
- Pineapple and Lime

Plus separately a cocktail range including;
- Fruit Tingle
- Espresso Martini
- Lifesaver
- Splice
- Passionfruit Gin and Tonic
- Signature Gin and Tonic

Can specifications attached

3.5% ALC/VOL
250ml Cans

Target Market(s)

25-35 Mainly Female

Industry/Entity Type

Alcoholic Beverages

Requirements
Must have
• Clear logo, room for a barcode to be added, 250ml and 3.5% ALC/VOL on the front centre, Australian pregnancy warning logo see attachments, 0.79 standard drink logo, simple description, "Produced By: Torla Distillery Pty Ltd 6/31 Quarrystone Drive Kellmoor NSW 2291"
Nice to have
• Simple consistent design for the range, fresh look, vibrant
Should not have
• Cartoon characters or anything perceived to be attractive to minors

```html
<!DOCTYPE html>
<html lang="en">
<head>
<meta charset="utf-8">
<title>Torla Distillery – Raspberry Vodka Soda Can Label</title>
<link rel="stylesheet" href="https://fonts.googleapis.com/css2?family=Great+Vibes&family=Montserrat:wght@400;500;600&display=swap">
<style>
  :root {
    --backdrop: #d9d9d9;
    --divider: #eeeeee;
    --label-white: #fbf8f9;
    --blush: #f3b3c0;
    --rose: #ee5a86;
    --hot-pink: #e5115f;
    --crimson: #9c1838;
    --plum: #7b1e7c;
    --indigo: #2d2c7c;
    --ink-light: #f6eef2;
    --ink-muted: #e8cfe0;
    --logo-ink: #6a1737;
    --barcode-panel: #3a1036;
    --info-ink: #fde6ef;
    --badge-dark: #1a1a1a;
    --warning-red: #c8102e;
  }
  * { box-sizing: border-box; margin: 0; padding: 0; }
  html, body { width: 1200px; height: 1021px; overflow: hidden; }
  body {
    background: var(--backdrop);
    font-family: "Montserrat", sans-serif;
  }
  .canvas {
    position: relative;
    width: 1200px;
    height: 1021px;
    display: grid;
    grid-template-columns: 1fr 1fr;
  }
  .canvas::after {
    content: "";
    position: absolute;
    left: 599px; top: 0;
    width: 3px; height: 100%;
    background: var(--divider);
  }
  .view {
    display: flex;
    align-items: center;
    justify-content: center;
  }
  .label {
    position: relative;
    width: 420px;
    height: 820px;
    border-radius: 6px;
    overflow: hidden;
    background:
      radial-gradient(ellipse 70% 22% at 22% 100%, rgba(45,44,124,0.95), rgba(45,44,124,0) 100%),
      radial-gradient(ellipse 60% 30% at 80% 62%, rgba(156,24,56,0.55), rgba(156,24,56,0) 100%),
      linear-gradient(180deg,
        var(--label-white) 0%,
        var(--label-white) 14%,
        var(--blush) 28%,
        var(--rose) 42%,
        var(--hot-pink) 56%,
        var(--crimson) 72%,
        var(--plum) 88%,
        #4b1a5c 100%);
  }
  /* front */
  .brand-name {
    position: absolute;
    top: 190px; left: 0; right: 0;
    text-align: center;
    font-weight: 500;
    font-size: 30px;
    letter-spacing: 0.5px;
    color: var(--logo-ink);
  }
  .flavour-name {
    position: absolute;
    top: 300px; left: 0; right: 0;
    text-align: center;
    font-family: "Great Vibes", cursive;
    font-size: 96px;
    line-height: 1.1;
    color: var(--ink-light);
  }
  .fruit-art {
    position: absolute;
    top: 470px; left: 150px;
    width: 120px; height: 140px;
    border-radius: 50% 50% 48% 48% / 40% 40% 60% 60%;
    background: radial-gradient(circle at 50% 40%, rgba(255,255,255,0.35), rgba(255,255,255,0.12));
  }
  .product-type {
    position: absolute;
    top: 650px; left: 0; right: 0;
    text-align: center;
    font-weight: 500;
    font-size: 26px;
    letter-spacing: 4px;
    color: var(--ink-muted);
  }
  .volume, .abv {
    position: absolute;
    bottom: 28px;
    font-size: 18px;
    color: var(--ink-muted);
  }
  .volume { left: 26px; }
  .abv { right: 26px; letter-spacing: 0.5px; }
  /* back */
  .producer {
    position: absolute;
    top: 500px; left: 26px;
    width: 228px;
    font-size: 15px;
    line-height: 1.35;
    color: var(--info-ink);
  }
  .standard-drinks {
    position: absolute;
    top: 505px; left: 268px;
    width: 54px; height: 66px;
    background: var(--badge-dark);
    clip-path: polygon(0 0, 100% 0, 100% 70%, 50% 100%, 0 70%);
  }
  .pregnancy-warning {
    position: absolute;
    top: 530px; left: 338px;
    width: 56px; height: 56px;
    border-radius: 50%;
    border: 3px solid var(--warning-red);
    background: rgba(0,0,0,0.15);
  }
  .barcode-space {
    position: absolute;
    top: 610px; left: 26px;
    width: 310px; height: 170px;
    background: linear-gradient(160deg, #5d1040, var(--barcode-panel) 70%, #22102e);
  }
</style>
</head>
<body>
  <main class="canvas">
    <section class="view view--front">
      <div class="label label--front">
        <div class="brand-name">Torla Distillery</div>
        <div class="flavour-name">Raspberry</div>
        <div class="fruit-art" role="img" aria-label="Line illustration of a raspberry"></div>
        <div class="product-type">VODKA SODA</div>
        <div class="volume">250ml</div>
        <div class="abv">3.5% ALC/VOL</div>
      </div>
    </section>
    <section class="view view--back">
      <div class="label label--back">
        <p class="producer">Produced By: Torla Distillery Pty Ltd 6/31 Quarrystone Drive Kellmoor NSW 2291</p>
        <div class="standard-drinks" role="img" aria-label="Standard drinks badge"></div>
        <div class="pregnancy-warning" role="img" aria-label="Pregnancy warning symbol"></div>
        <div class="barcode-space" aria-label="Space reserved for barcode"></div>
      </div>
    </section>
  </main>
</body>
</html>
```